Business Card Design

We are a radiology group

We are working to move into new service centers

We want to communicate innovation and bringing our customers ahead with technology and outstanding results

I have uploaded a high resolution logo as requested :-)

Target Market(s)

hospitals, clinics

Industry/Entity Type

Business

Contact Information for Business Card

Linda R. Feathersby, MBA, CIIP
CTIO
linda.feathersby@trovexa-rad.com
cell 607-481-2937
www.trovexa-rad.com
Trovexa Radiology Partners, PC

```html
<!DOCTYPE html>
<html lang="en">
<head>
<meta charset="utf-8">
<title>Trovexa Radiology Partners – Business Card</title>
<link rel="stylesheet" href="https://fonts.googleapis.com/css2?family=Mulish:wght@400;600;700;800&display=swap">
<style>
  :root {
    --backdrop: #e9eaec;
    --card: #ffffff;
    --band: #aad9f1;
    --ink-blue: #1e4f7d;
    --ink-grey: #6b6d70;
    --ink-dark: #222428;
    --rule: #8a8c8f;
  }
  * { box-sizing: border-box; margin: 0; padding: 0; }
  html, body {
    width: 1200px; height: 549px; overflow: hidden;
    background: var(--backdrop);
    font-family: "Mulish", "Century Gothic", sans-serif;
  }
  .card {
    position: absolute; left: 180px; top: 34px;
    width: 840px; height: 480px;
    background: var(--card);
    box-shadow: 0 10px 28px rgba(0,0,0,.18);
    overflow: hidden;
  }
  .card__header {
    position: absolute; left: 0; top: 0; width: 100%; height: 78px;
    background: var(--band);
    display: flex; align-items: center; justify-content: flex-end;
    padding-right: 60px;
  }
  .card__header-title {
    font-weight: 700; font-size: 32px; letter-spacing: 1.5px;
    font-variant: small-caps; color: var(--ink-grey);
  }
  .name-tab {
    position: absolute; left: 0; top: 104px;
    height: 42px; padding: 0 30px 0 26px;
    background: var(--band); border-radius: 0 14px 14px 0;
    display: flex; align-items: center;
  }
  .name-tab__name {
    font-weight: 800; font-size: 22px; color: #3a4a5a; letter-spacing: .4px;
  }
  .credentials {
    position: absolute; left: 26px; top: 156px;
    font-size: 14px; color: var(--ink-grey); letter-spacing: .5px;
  }
  .contact-list { position: absolute; left: 26px; top: 192px; list-style: none; }
  .contact-list__item {
    display: flex; align-items: flex-start; gap: 14px;
    margin-bottom: 20px;
    font-weight: 700; font-size: 17px; color: var(--ink-blue); line-height: 1.25;
  }
  .contact-list__icon { width: 22px; height: 22px; flex: none; fill: var(--ink-blue); }
  .divider {
    position: absolute; left: 468px; top: 110px;
    width: 2px; height: 230px; background: var(--rule);
  }
  .brand {
    position: absolute; left: 500px; top: 200px; width: 320px;
    display: flex; align-items: center; gap: 12px;
  }
  .brand__dot { width: 16px; height: 16px; border-radius: 50%; background: var(--band); flex: none; }
  .brand__name {
    font-weight: 600; font-size: 20px; color: var(--ink-grey); letter-spacing: .6px;
  }
  .card__footer {
    position: absolute; left: 0; bottom: 0; width: 100%; height: 118px;
    background: var(--band);
  }
  .card__footer-strip {
    position: absolute; left: 0; top: 14px; width: 100%; height: 52px;
    background: var(--card);
    display: flex; align-items: center; justify-content: center;
  }
  .website { font-weight: 800; font-size: 23px; color: var(--ink-dark); letter-spacing: .3px; }
</style>
</head>
<body>
  <article class="card">
    <header class="card__header">
      <span class="card__header-title">Trovexa Radiology Partners</span>
    </header>

    <div class="name-tab"><span class="name-tab__name">Linda R. Feathersby</span></div>
    <p class="credentials">MBA, CIIP CTIO</p>

    <ul class="contact-list">
      <li class="contact-list__item">
        <svg class="contact-list__icon" viewBox="0 0 24 24" aria-hidden="true">
          <path d="M7 1h10a2 2 0 0 1 2 2v18a2 2 0 0 1-2 2H7a2 2 0 0 1-2-2V3a2 2 0 0 1 2-2zm0 3v14h10V4H7zm5 15.5a1.2 1.2 0 1 0 0 2.4 1.2 1.2 0 0 0 0-2.4z"/>
        </svg>
        <span>607-481-2937</span>
      </li>
      <li class="contact-list__item">
        <svg class="contact-list__icon" viewBox="0 0 24 24" aria-hidden="true">
          <path d="M2 5h20v14H2V5zm2 2v.4l8 5.4 8-5.4V7H4zm16 2.8-8 5.4-8-5.4V17h16V9.8z"/>
        </svg>
        <span>linda.feathersby@trovexa-rad.com</span>
      </li>
      <li class="contact-list__item">
        <svg class="contact-list__icon" viewBox="0 0 24 24" aria-hidden="true">
          <path d="M12 1a7 7 0 0 1 7 7c0 5.2-7 15-7 15S5 13.2 5 8a7 7 0 0 1 7-7zm0 4a3 3 0 1 0 0 6 3 3 0 0 0 0-6z"/>
        </svg>
        <span>240 N. Alder Avenue,<br>Fairholt CA 90218</span>
      </li>
    </ul>

    <div class="divider"></div>

    <div class="brand">
      <span class="brand__dot"></span>
      <span class="brand__name">Trovexa Radiology Partners</span>
    </div>

    <footer class="card__footer">
      <div class="card__footer-strip">
        <span class="website">www.trovexa-rad.com</span>
      </div>
    </footer>
  </article>
</body>
</html>
```